Im starting a new speed dating business, called 'lantern speed dating', in my local area. I'm looking

I live in a semi-rural, quite alternative & progressive, spiritual community (Byron Bay, Australia). I want to launch the first event in 4 weeks! I would like a design for a flyer that catches people's attention, not in a 'screaming' way, but beautiful, interesting, inviting......They'll be monthly events, possibly with different themes; silent, tantric, spiritual.....etc.
I like to create a 'brand', where design for flyer, website, Fb, logo is aligned and easily recognizable.
The singles events are to be safe, sacred, playful, deep, fun & well facilitated.
It's for people serious about meeting & connecting authentically with others, with an interest to partner. Thank you
Single men & women, intelligent, conscious, middle class, 25-55yrs
Dating

```html
<!DOCTYPE html>
<html lang="en">
<head>
<meta charset="utf-8">
<title>Lantern Speed Dating</title>
<link rel="stylesheet" href="https://fonts.googleapis.com/css2?family=Roboto:ital,wght@1,900&display=swap">
<style>
  :root {
    --lavender: #c39cf0;
    --violet: #a765e6;
    --night: #000000;
    --sun: #fff200;
    --heart-red: #c8161d;
    --heart-deep: #8a0c10;
    --heart-edge: #5e0608;
    --arrow-white: #ffffff;
    --title-top: #ffffff;
    --title-mid: #d98cf5;
    --title-deep: #8a10c8;
    --ring-light: #f0a8ff;
    --ring-deep: #8a1fb5;
  }
  html, body {
    margin: 0;
    padding: 0;
    overflow: hidden;
    background: var(--night);
  }
  .flyer {
    position: relative;
    width: 848px;
    height: 1200px;
    overflow: hidden;
  }
  .flyer-art {
    display: block;
    width: 848px;
    height: 1200px;
  }
  .title-word {
    font-family: "Roboto", Arial, sans-serif;
    font-style: italic;
    font-weight: 900;
    font-size: 96px;
    fill: url(#title-fill);
    filter: drop-shadow(5px 6px 3px rgba(0, 0, 0, 0.85));
  }
  .grid-line {
    stroke: var(--night);
    stroke-width: 13;
    fill: none;
  }
  .arrow-shaft {
    stroke: var(--arrow-white);
    stroke-width: 4;
  }
  .arrow-head,
  .arrow-fletch {
    fill: var(--arrow-white);
    stroke: #bfbfbf;
    stroke-width: 1;
  }
  .heart-cluster {
    fill: url(#hearts-fill);
    stroke: var(--heart-edge);
    stroke-width: 3;
  }
</style>
</head>
<body>
<main class="flyer">
  <svg class="flyer-art" viewBox="0 0 826 1169" preserveAspectRatio="none" xmlns="http://www.w3.org/2000/svg">
    <defs>
      <linearGradient id="title-fill" x1="0" y1="0" x2="0" y2="1">
        <stop offset="0" stop-color="var(--title-top)"/>
        <stop offset="0.45" stop-color="var(--title-mid)"/>
        <stop offset="1" stop-color="var(--title-deep)"/>
      </linearGradient>
      <linearGradient id="hearts-fill" x1="0" y1="0" x2="0.4" y2="1">
        <stop offset="0" stop-color="var(--heart-red)"/>
        <stop offset="1" stop-color="var(--heart-deep)"/>
      </linearGradient>
      <linearGradient id="ring-fill" x1="0" y1="0" x2="1" y2="1">
        <stop offset="0" stop-color="var(--ring-light)"/>
        <stop offset="1" stop-color="var(--ring-deep)"/>
      </linearGradient>
    </defs>

    <!-- background fields -->
    <rect class="field-night" width="826" height="1169" fill="var(--night)"/>
    <polygon class="field-lavender" points="0,0 380,0 0,195" fill="var(--lavender)"/>
    <polygon class="field-violet" points="826,835 826,1169 120,1169" fill="var(--violet)"/>

    <!-- tilted yellow grid -->
    <g class="floor-grid">
      <polygon points="20,330 545,25 880,720 95,1010" fill="var(--sun)"/>
      <polygon class="grid-line" points="20,330 545,25 880,720 95,1010"/>
      <line class="grid-line" x1="125" y1="269" x2="252" y2="952"/>
      <line class="grid-line" x1="230" y1="208" x2="409" y2="894"/>
      <line class="grid-line" x1="335" y1="147" x2="566" y2="836"/>
      <line class="grid-line" x1="440" y1="86" x2="723" y2="778"/>
      <line class="grid-line" x1="31" y1="427" x2="593" y2="124"/>
      <line class="grid-line" x1="41" y1="524" x2="641" y2="224"/>
      <line class="grid-line" x1="52" y1="621" x2="689" y2="323"/>
      <line class="grid-line" x1="63" y1="719" x2="736" y2="422"/>
      <line class="grid-line" x1="74" y1="816" x2="784" y2="521"/>
      <line class="grid-line" x1="84" y1="913" x2="832" y2="621"/>
    </g>

    <!-- heart clusters -->
    <rect class="heart-cluster hearts-upper" role="img" aria-label="Cluster of glossy red hearts with small outlined hearts" x="515" y="148" width="275" height="255" rx="70"/>
    <rect class="heart-cluster hearts-lower" role="img" aria-label="Cluster of glossy red hearts with small outlined hearts" x="78" y="668" width="282" height="228" rx="70"/>

    <!-- gender icon -->
    <g class="gender-icon">
      <circle cx="74" cy="215" r="28" fill="none" stroke="var(--arrow-white)" stroke-width="9"/>
      <line x1="74" y1="243" x2="74" y2="295" stroke="var(--arrow-white)" stroke-width="9"/>
      <line x1="50" y1="268" x2="98" y2="268" stroke="var(--arrow-white)" stroke-width="9"/>
      <circle cx="92" cy="198" r="26" fill="none" stroke="var(--heart-red)" stroke-width="7"/>
      <line x1="110" y1="217" x2="145" y2="250" stroke="var(--heart-red)" stroke-width="6"/>
      <polygon points="152,257 128,252 147,233" fill="var(--heart-red)"/>
    </g>

    <!-- arrows -->
    <g class="arrow arrow-right-top">
      <line class="arrow-shaft" x1="0" y1="362" x2="520" y2="362"/>
      <polygon class="arrow-head" points="548,362 420,338 440,362 420,386"/>
      <polygon class="arrow-fletch" points="0,342 60,362 0,382 20,362"/>
    </g>
    <g class="arrow arrow-left">
      <line class="arrow-shaft" x1="110" y1="490" x2="690" y2="490"/>
      <polygon class="arrow-head" points="85,490 210,466 190,490 210,514"/>
      <polygon class="arrow-fletch" points="580,470 690,478 640,490 690,502 580,510 620,490"/>
    </g>
    <g class="arrow arrow-right-bottom">
      <line class="arrow-shaft" x1="235" y1="620" x2="790" y2="620"/>
      <polygon class="arrow-head" points="815,620 700,598 718,620 700,642"/>
      <polygon class="arrow-fletch" points="235,600 345,612 300,620 345,628 235,640 275,620"/>
    </g>

    <!-- title -->
    <text class="title-word" x="78" y="354" textLength="335" lengthAdjust="spacingAndGlyphs">Lantern</text>
    <text class="title-word" x="200" y="480" textLength="335" lengthAdjust="spacingAndGlyphs">Speed</text>
    <text class="title-word" x="342" y="606" textLength="375" lengthAdjust="spacingAndGlyphs">Dating</text>

    <!-- corner rings -->
    <g class="corner-rings" fill="none">
      <circle cx="160" cy="1260" r="185" stroke="url(#ring-fill)" stroke-width="40"/>
      <circle cx="150" cy="1250" r="95" stroke="url(#ring-fill)" stroke-width="26"/>
    </g>
  </svg>
</main>
</body>
</html>
```